Sticker for Scrap Metal Bin that is placed at customers premises

During the course of our operation, Scrap Metal Bin are place at our customer site for them to dispose scrap metal into the Bin.

Would like to have a sticker for us to paste on the bin.

All scrap bin will be blue color. Attached sample of current sticker on a scrap bin.

Would like one that is clean, simple and eye catching also that the font is much visible unlike the current one that is cramp and small.

Target Market(s)

Businesses

Font styles to use
Serif

Requirements
Must have
• 1) Company Name and Logo
• 2) Contact Details : 9314 5520 / 6283 4057
• 3) Website: www.korvalenmetals.com

```html
<!DOCTYPE html>
<html lang="en">
<head>
<meta charset="UTF-8">
<title>Korvalen Metals – Bin Sticker</title>
<link href="https://fonts.googleapis.com/css2?family=Tinos:wght@400;700&display=swap" rel="stylesheet">
<style>
  :root {
    --bin-blue: #2b88b5;
    --sticker-white: #fdfcfa;
    --gold: #c9982f;
    --gold-deep: #b07f1c;
    --ink: #111111;
  }
  * { margin: 0; padding: 0; box-sizing: border-box; }
  html, body {
    width: 1200px;
    height: 1200px;
    overflow: hidden;
  }
  body {
    background: var(--bin-blue);
    display: flex;
    align-items: center;
    justify-content: center;
    font-family: "Tinos", "Times New Roman", serif;
  }
  .sticker {
    width: 900px;
    height: 900px;
    background: var(--sticker-white);
    border: 10px solid var(--gold);
    box-shadow: inset 0 0 0 2px var(--gold-deep);
    display: flex;
    flex-direction: column;
    align-items: center;
    color: var(--ink);
  }
  .brand {
    margin-top: 150px;
    display: flex;
    flex-direction: column;
    align-items: center;
  }
  .brand-mark {
    width: 120px;
    height: 120px;
    border: 6px solid var(--gold);
  }
  .brand-name {
    margin-top: 48px;
    font-size: 58px;
    font-weight: 700;
    letter-spacing: 2px;
    color: var(--gold);
    text-transform: uppercase;
    line-height: 1;
  }
  .brand-tagline {
    margin-top: 14px;
    font-size: 26px;
    font-weight: 700;
    letter-spacing: 4px;
    color: var(--ink);
    text-transform: uppercase;
  }
  .contact-phone {
    margin-top: 90px;
    font-size: 64px;
    font-weight: 700;
    letter-spacing: 1px;
  }
  .contact-web {
    margin-top: 120px;
    font-size: 40px;
    font-weight: 700;
    letter-spacing: 2px;
    text-transform: uppercase;
  }
</style>
</head>
<body>
  <main class="sticker">
    <div class="brand">
      <div class="brand-mark"></div>
      <p class="brand-name">Korvalen Metals</p>
      <p class="brand-tagline">Recycling</p>
    </div>
    <p class="contact-phone">9314 5520 / 6283 4057</p>
    <p class="contact-web">www.korvalenmetals.com</p>
  </main>
</body>
</html>
```